Postcard for Funeral Homes

We need a double-sided postcard 8.5" x 5.5" to be sent to the Directors of Funeral Homes advising them of our White Dove Releases for funerals and memorial services. This is a business to business marketing piece that we are using to introduce Lantern Glow Tributes services to Funeral Homes.

Lantern Glow Tributes is the originator of White Dove Releases in the Greater Toronto Area. A professional White Dove Release is a beautiful tribute to the lives of those who are no longer with us, expressing peace for the one who has moved on and comfort for those who remain. Releasing the White Doves and watching as they soar upwards to the heavens provides a spiritually uplifting moment during a time of grief.

A single White Dove is released first, representing the spirit of the deceased transcending from one state to another. The single Dove is followed by a flock of White Doves, nestled in and released from special white latticework pillars.

We want to communicate that White Dove Releases should be included in the options available through the Funeral Homes when arrangements are being made by the family of the deceased.

The design should convey professionalism and dependability in addition to being graceful, beautiful and spiritually comforting (without any reference to a particular religion). For more information what Lantern Glow Tributes offers, please visit www.lanternglowtributes.com

Target Market(s)

We are targeting the Directors of Funeral Homes and Cemeteries who make decisions on what services and arrangements to offer the families of the deceased.

Requirements
Must have
• The design must have space for us to affix mailing labels and a stamp.
• There should be Images of White Doves and dove releases at cemeteries.
• Text for the front and back of the postcard has been provided.
Should not have
• There cannot be any religious images or specific religious symbols

```html
<!DOCTYPE html>
<html lang="en">
<head>
<meta charset="utf-8">
<title>Lantern Glow Tributes – Postcard</title>
<link rel="stylesheet" href="https://fonts.googleapis.com/css2?family=Cinzel:wght@400&family=Open+Sans:wght@400;600&display=swap">
<style>
  :root {
    --page: #ffffff;
    --front-light: #9a9a9a;
    --front-dark: #3e3e3e;
    --band-light: #8a8a8a;
    --band-dark: #505050;
    --back-black: #050505;
    --text-white: #ffffff;
    --text-soft: #d4d4d4;
    --text-muted: #bdbdbd;
  }
  * { margin: 0; padding: 0; box-sizing: border-box; }
  html, body {
    width: 1200px; height: 1000px; overflow: hidden;
    background: var(--page);
  }
  .canvas { position: relative; width: 1200px; height: 1000px; }

  .card { position: absolute; left: 305px; width: 638px; height: 414px; overflow: hidden; }

  /* Front */
  .card--front {
    top: 73px;
    background: radial-gradient(ellipse 55% 70% at 50% 55%, var(--front-light) 0%, #6c6c6c 55%, var(--front-dark) 100%);
  }
  .brand {
    position: absolute; left: 0; right: 0; top: 168px;
    display: flex; align-items: center; justify-content: center; gap: 16px;
  }
  .brand__dot { width: 18px; height: 18px; border-radius: 50%; background: var(--text-white); }
  .brand__name {
    font-family: "Cinzel", serif; font-weight: 400;
    font-size: 36px; letter-spacing: 2px; color: var(--text-white);
  }
  .tagline {
    position: absolute; left: 0; right: 0; top: 266px; text-align: center;
    font-family: "Cinzel", serif; font-size: 13px; letter-spacing: 3px;
    color: var(--text-white);
  }

  /* Back */
  .card--back { top: 517px; background: var(--back-black); }
  .back__band {
    position: absolute; left: 0; top: 0; width: 100%; height: 106px;
    background: linear-gradient(180deg, var(--band-light) 0%, #6a6a6a 60%, var(--band-dark) 100%);
  }
  .back__title {
    position: absolute; left: 39px; top: 30px;
    font-family: "Open Sans", sans-serif; font-size: 25px; font-weight: 400;
    line-height: 34px; color: var(--text-white);
  }
  .back__subtitle {
    position: absolute; left: 39px; top: 68px;
    font-family: "Open Sans", sans-serif; font-size: 11px; color: var(--text-white);
  }
  .dove-photo {
    position: absolute; left: 315px; top: 40px; width: 323px; height: 360px;
    background:
      linear-gradient(135deg, rgba(255,255,255,0) 40%, rgba(255,255,255,0.25) 55%, rgba(255,255,255,0) 70%),
      radial-gradient(ellipse 38% 48% at 45% 52%, #f2f2f2 0%, #bdbdbd 35%, rgba(40,40,40,0.4) 70%, rgba(5,5,5,0) 100%);
  }
  .back__lead {
    position: absolute; left: 37px; top: 150px; width: 300px;
    font-family: "Open Sans", sans-serif; font-size: 14.5px; line-height: 21px;
    color: var(--text-soft);
  }
  .features {
    position: absolute; left: 38px; top: 224px; list-style: none;
    font-family: "Open Sans", sans-serif; font-size: 10px;
    color: var(--text-muted);
  }
  .features li { display: block; height: 22px; line-height: 22px; white-space: nowrap; }
  .features li::before { content: "\2756"; margin-right: 5px; font-size: 8px; vertical-align: 1px; }
  .contact {
    position: absolute; right: 22px; top: 354px; text-align: right;
    font-family: "Open Sans", sans-serif; font-size: 10px; font-weight: 400;
    line-height: 13.5px; font-style: normal; color: var(--text-white);
  }
</style>
</head>
<body>
<div class="canvas">

  <section class="card card--front">
    <div class="brand">
      <span class="brand__dot"></span>
      <span class="brand__name">Lantern Glow Tributes</span>
    </div>
    <p class="tagline">FAMILY HEALING SINCE 1995</p>
  </section>

  <section class="card card--back">
    <div class="back__band"></div>
    <h1 class="back__title">Lantern Glow Tributes</h1>
    <p class="back__subtitle">Honouring the Deceased. Comforting the Living.</p>

    <div class="dove-photo" role="img" aria-label="Photograph of a white dove in flight with wings raised, lit by soft rays of light against a dark background"></div>

    <p class="back__lead">Serving the needs of funeral homes and cemeteries for more than 15 years.</p>

    <ul class="features">
      <li>Spiritual complement to burial, cremation, and memorial services</li>
      <li>Symbolizes the spirit transcending from one state to another</li>
      <li>Non-denominational, multi-cultural</li>
      <li>Appropriate for traditional and non-traditional services</li>
      <li>Professional, courteous and dependable staff</li>
      <li>Staff is always on time and appropriately dressed</li>
      <li>Non-intrusive set up prior to family’s arrival</li>
      <li>Poems and readings available</li>
    </ul>

    <address class="contact">
      For more information contact<br>
      Dana 416.555-0148<br>
      info@lanternglowtributes.com | www.lanternglowtributes.com
    </address>
  </section>

</div>
</body>
</html>
```